High End Art Gallery Business Card

We're looking for a business card design that is elegant and artful. Foil embossing, blind embossed pattern, or some kind of "extra" element to make it stand out. Standard American size. The back should remain blank or nearly blank so that notes can be written on the back.
Please check our website at elsintandor.com to see information about our gallery and the type of artwork that we sell.
Included with the files is a brand identity guideline. In addition to the colors listed, we like to incorporate an indigo blue. The business card design in the guideline seems too simplistic. I have included some photos of other business card designs that have caught my eye.
thank you!

Contact Information for Business Card

Mirela Tandor
Gallery Owner
remaining details are in the attached docs

Requirements
Nice to have
• some kind of natural/organic element to reflect the hand-made nature of all of the original artwork.

```html
<!DOCTYPE html>
<html lang="en">
<head>
<meta charset="utf-8">
<title>Elsin Tandor of Lanikai Gallery — Business Card</title>
<link href="https://fonts.googleapis.com/css2?family=Open+Sans:wght@400;600;700&display=swap" rel="stylesheet">
<style>
  :root {
    --backdrop: #2e2926;
    --card: #141414;
    --card-edge: #1d1d1d;
    --gold: #a88a55;
    --ink: #f2f2f2;
    --muted: #bdbdbd;
    --rule: #d9d9d9;
  }
  * { box-sizing: border-box; margin: 0; padding: 0; }
  html, body {
    width: 1200px; height: 864px; overflow: hidden;
    background: var(--backdrop);
    font-family: "Open Sans", Arial, sans-serif;
  }
  .canvas { position: relative; width: 1200px; height: 864px; }
  .card {
    position: absolute; width: 490px; height: 280px;
    background: var(--card);
    border: 1px solid var(--card-edge);
    box-shadow: 0 10px 30px rgba(0,0,0,.45);
  }
  .card--back { left: 70px; top: 140px; }
  .card--front { left: 640px; top: 420px; }

  /* Back side */
  .back-lockup {
    position: absolute; left: 0; right: 0; top: 58px;
    display: flex; flex-direction: column; align-items: center; text-align: center;
  }
  .brand-dot {
    width: 74px; height: 74px; border-radius: 50%;
    background: var(--gold);
  }
  .brand-name {
    color: var(--ink); font-weight: 400; text-transform: uppercase;
    letter-spacing: .08em; line-height: 1.25;
  }
  .back-lockup .brand-name { margin-top: 14px; font-size: 15px; }
  .brand-tagline {
    color: var(--muted); font-size: 7px; letter-spacing: .2em;
    text-transform: uppercase; margin-top: 3px;
  }
  .back-url {
    margin-top: 16px; color: var(--muted); font-size: 11px; letter-spacing: .22em;
  }

  /* Front side */
  .front-lockup {
    position: absolute; right: 26px; top: 44px;
    display: flex; align-items: center; gap: 12px;
  }
  .front-lockup .brand-dot { width: 58px; height: 58px; }
  .front-lockup .brand-name { font-size: 13px; }
  .front-lockup .brand-tagline { font-size: 6px; }

  .person { position: absolute; left: 30px; top: 92px; }
  .person-name {
    color: var(--gold); font-weight: 700; font-size: 17px;
    text-transform: uppercase; letter-spacing: .02em;
  }
  .person-role { color: var(--ink); font-size: 11px; text-transform: uppercase; margin-top: 1px; }

  .divider {
    position: absolute; left: 30px; right: 26px; top: 140px;
    height: 1px; background: var(--rule);
  }
  .contacts {
    position: absolute; left: 30px; top: 150px; list-style: none;
    color: var(--ink); font-size: 12px; line-height: 19px;
  }
  .contacts li { display: flex; align-items: center; gap: 7px; }
  .contacts svg { width: 11px; height: 11px; fill: var(--gold); flex: none; }

  .address-rule {
    position: absolute; right: 26px; top: 200px; width: 160px;
    height: 1px; background: var(--rule);
  }
  .address {
    position: absolute; right: 26px; top: 208px; text-align: right;
    color: var(--ink); font-size: 12.5px; line-height: 17px; font-style: normal;
  }
</style>
</head>
<body>
<main class="canvas">

  <section class="card card--back" aria-label="Card back">
    <div class="back-lockup">
      <div class="brand-dot"></div>
      <p class="brand-name">Elsin Tandor of<br>Lanikai Gallery</p>
      <p class="brand-tagline">Fine art of Asia &amp; the Pacific</p>
      <p class="back-url">www.elsintandor.com</p>
    </div>
  </section>

  <section class="card card--front" aria-label="Card front">
    <div class="front-lockup">
      <div class="brand-dot"></div>
      <div>
        <p class="brand-name">Elsin Tandor of<br>Lanikai Gallery</p>
        <p class="brand-tagline">Fine art of Asia &amp; the Pacific</p>
      </div>
    </div>

    <div class="person">
      <h1 class="person-name">Mirela Tandor</h1>
      <p class="person-role">Co-Owner</p>
    </div>

    <div class="divider"></div>

    <ul class="contacts">
      <li>
        <svg viewBox="0 0 24 24" aria-hidden="true"><path d="M6.6 10.8a15 15 0 0 0 6.6 6.6l2.2-2.2a1 1 0 0 1 1-.25 11.4 11.4 0 0 0 3.6.57 1 1 0 0 1 1 1V20a1 1 0 0 1-1 1A17 17 0 0 1 3 4a1 1 0 0 1 1-1h3.5a1 1 0 0 1 1 1c0 1.25.2 2.46.57 3.6a1 1 0 0 1-.25 1z"/></svg>
        555-214-0382
      </li>
      <li>
        <svg viewBox="0 0 24 24" aria-hidden="true"><rect x="5" y="2" width="14" height="20" rx="2"/></svg>
        555-730-4416
      </li>
      <li>
        <svg viewBox="0 0 24 24" aria-hidden="true"><path d="M2 5h20v14H2z M2 5l10 8 10-8" /></svg>
        info@elsintandor.com
      </li>
    </ul>

    <div class="address-rule"></div>
    <address class="address">
      312 Kealoha Street<br>
      Hilo, Hawaii 96720<br>
      www.elsintandor.com
    </address>
  </section>

</main>
</body>
</html>
```